Business Card Design Project

I want a design for my business cards based on an excisting logo design.

Target Market(s)

Marketeers, PR-peeps, CEO's, decisionmakers, entrepreneurs

Industry/Entity Type

Business

Requirements
Nice to have
• Some visual interest on the back too
Should not have
• Sarif on the font

```html
<!DOCTYPE html>
<html lang="nl">
<head>
<meta charset="utf-8">
<title>LeafLine PR – visitekaartjes</title>
<link rel="stylesheet" href="https://fonts.googleapis.com/css2?family=Questrial&display=swap">
<style>
  :root {
    --bg: #e9e7e3;
    --card: #ffffff;
    --card-shade: #f2f2f2;
    --green: #8cc63f;
    --green-dark: #1f9a3a;
    --grey: #6d6e71;
    --ink: #333333;
  }
  * { box-sizing: border-box; margin: 0; padding: 0; }
  html, body { width: 1200px; height: 951px; overflow: hidden; }
  body {
    background: var(--bg);
    font-family: "Questrial", "Century Gothic", sans-serif;
    color: var(--ink);
    position: relative;
  }
  .card {
    position: absolute;
    width: 580px;
    height: 352px;
    border-radius: 22px;
    background: linear-gradient(160deg, var(--card) 55%, var(--card-shade));
    box-shadow: 0 10px 28px rgba(0,0,0,.18);
    overflow: hidden;
  }
  .card--front { left: 70px; top: 70px; }
  .card--back { left: 550px; top: 520px; }

  .brand { display: flex; align-items: center; gap: 16px; color: var(--grey); white-space: nowrap; }
  .brand__dot { border-radius: 50%; background: var(--green); flex: none; }

  .card--front .brand {
    position: absolute; left: 0; right: 0; top: 86px;
    flex-direction: column; gap: 22px;
  }
  .card--front .brand__dot { width: 120px; height: 120px; }
  .card--front .brand__name { font-size: 48px; letter-spacing: 1px; }
  .tagline {
    position: absolute; left: 0; right: 0; bottom: 34px;
    text-align: center; font-size: 17px; color: var(--ink);
  }

  .swoosh { position: absolute; left: 0; top: 0; width: 580px; height: 352px; }

  .card--back .brand { position: absolute; left: 150px; top: 46px; }
  .card--back .brand__dot { width: 50px; height: 50px; }
  .card--back .brand__name { font-size: 46px; letter-spacing: 1px; }

  .contact {
    position: absolute; left: 34px; top: 170px;
    list-style: none; font-size: 17px; line-height: 1.2;
  }
  .contact li { display: flex; gap: 10px; margin-bottom: 6px; }
  .contact svg { width: 16px; height: 16px; flex: none; margin-top: 2px; fill: var(--green); }

  .person {
    position: absolute; left: 330px; top: 218px;
    font-size: 24px; color: var(--green);
  }
  .social {
    position: absolute; left: 330px; top: 272px;
    list-style: none; font-size: 17px; line-height: 1.3;
  }
</style>
</head>
<body>

<section class="card card--front" aria-label="Voorkant visitekaartje">
  <div class="brand">
    <span class="brand__dot"></span>
    <span class="brand__name">LeafLine PR</span>
  </div>
  <p class="tagline">Systemisch en strategisch PR • Marketing • En communicatieadvies</p>
</section>

<section class="card card--back" aria-label="Achterkant visitekaartje">
  <svg class="swoosh" viewBox="0 0 580 352" aria-hidden="true">
    <path d="M0 0 H120 Q40 20 0 70 Z" fill="var(--green-dark)"/>
    <path d="M0 78 Q50 24 135 0 H150 Q60 26 0 92 Z" fill="var(--green)"/>
    <path d="M580 352 H460 Q540 330 580 282 Z" fill="var(--green-dark)"/>
    <path d="M580 272 Q530 326 445 352 H430 Q520 326 580 258 Z" fill="var(--green)"/>
  </svg>

  <div class="brand">
    <span class="brand__dot"></span>
    <span class="brand__name">LeafLine PR</span>
  </div>

  <ul class="contact">
    <li>
      <svg viewBox="0 0 16 16"><path d="M8 1 L15 8 H13 V15 H10 V10 H6 V15 H3 V8 H1 Z"/></svg>
      <span>Lindelaan 12<br>6711 AB Ede</span>
    </li>
    <li>
      <svg viewBox="0 0 16 16"><path d="M4 1 L6.5 4 L5 6 Q6.5 9.5 10 11 L12 9.5 L15 12 L13 15 Q3 13 1 3 Z"/></svg>
      <span>+31(0)6 20481935</span>
    </li>
    <li>
      <svg viewBox="0 0 16 16"><path d="M1 4 H15 V13 H1 Z M1 4 L8 9 L15 4" stroke="#fff" stroke-width="1"/></svg>
      <span>mara.jansen@leaflinepr.nl</span>
    </li>
    <li>
      <svg viewBox="0 0 16 16"><circle cx="8" cy="8" r="7"/></svg>
      <span>www.leaflinepr.nl</span>
    </li>
  </ul>

  <p class="person">Mara Jansen</p>
  <ul class="social">
    <li>twitter.com/_leaflinepr</li>
    <li>facebook.com/leaflinepr</li>
  </ul>
</section>

</body>
</html>
```